Paint Protection Options

This is a flyer that will describe two different paint protection options for vehicles. I have mocked up a Word doc. As well, I've included some samples of other flyers where I like the "look". I am not locked into any single layout or design. In my Word doc I have them side-by-side. I think that makes sense but open to ideas. I've also added some pics of the two options being applied to cars. We need to have one of each (ceramic and ppf) at a minimum. In the grid I'm thinking different colors dots/circles to differentiate the different levels. But again, I'm open to suggestions. You can use the symbol for microns in the grid under the Thickness row. I spelled it out because I didn't know how to insert.

```html
<!DOCTYPE html>
<html lang="en">
<head>
<meta charset="utf-8">
<title>Paint Protection Options</title>
<link rel="stylesheet" href="https://fonts.googleapis.com/css2?family=Bebas+Neue&family=Montserrat:wght@400;500;600&display=swap">
<style>
  :root {
    --backdrop: #b1b1b1;
    --paper: #ffffff;
    --red: #c8202a;
    --red-deep: #8c0d12;
    --red-dark: #5a0508;
    --ink: #151515;
    --cell-top: #ffffff;
    --cell-bottom: #e4e5e8;
  }
  * { box-sizing: border-box; margin: 0; padding: 0; }
  html, body { width: 930px; height: 1200px; overflow: hidden; background: var(--backdrop); }
  body { position: relative; font-family: "Montserrat", sans-serif; color: var(--ink); }

  .flyer {
    position: absolute; left: 107px; top: 93px; width: 717px; height: 1014px;
    background: var(--paper); overflow: hidden;
  }
  .hero { position: absolute; left: 0; top: 0; width: 717px; height: 260px; }
  .hero-title {
    position: absolute; left: 31px; top: 32px;
    font-family: "Bebas Neue", sans-serif; font-size: 66px; line-height: 56px;
    color: #fff; letter-spacing: 0.5px;
  }
  .hero-car { position: absolute; left: 340px; top: 18px; }

  .section-title {
    position: absolute; left: 29px;
    font-family: "Bebas Neue", sans-serif; font-size: 43px; line-height: 1; color: var(--ink);
  }
  .section-title .accent { color: var(--red); }
  .ceramic-title { top: 249px; }
  .ppf-title { top: 465px; }

  .section-text {
    position: absolute; left: 29px; width: 486px;
    font-size: 11.3px; line-height: 15.1px; text-align: justify;
  }
  .section-text p + p { margin-top: 15.1px; }
  .ceramic-text { top: 288px; }
  .ppf-text { top: 504px; }

  .photo-ring { position: absolute; }
  .ceramic-photo { left: 530px; top: 270px; }
  .ppf-photo { left: 530px; top: 474px; }

  .compare {
    position: absolute; left: 30px; top: 669px; width: 656px;
    display: grid; grid-template-columns: 188px 151px 151px 151px;
    grid-auto-rows: 22px; column-gap: 4.6px; row-gap: 2.7px;
    font-size: 9.3px; font-weight: 600;
  }
  .compare .head {
    background: linear-gradient(var(--red), var(--red-deep));
    color: #fff; display: flex; align-items: center; justify-content: center; font-weight: 500;
  }
  .compare .head.flat { background: var(--red); }
  .compare .feature {
    background: var(--red); color: #fff; display: flex; align-items: center;
    padding-left: 17px; font-weight: 500;
  }
  .compare .value {
    background: linear-gradient(var(--cell-top), var(--cell-bottom));
    display: flex; align-items: center; justify-content: center;
  }
</style>
</head>
<body>
<main class="flyer">
  <header class="hero">
    <svg width="717" height="260" viewBox="0 0 717 260" aria-hidden="true">
      <defs>
        <linearGradient id="heroRed" x1="0" y1="0" x2="1" y2="0">
          <stop offset="0" stop-color="#c41e26"/>
          <stop offset="0.6" stop-color="#a8121a"/>
          <stop offset="1" stop-color="#4d0204"/>
        </linearGradient>
      </defs>
      <path d="M0 0 H717 V205 C600 215 520 200 430 180 C300 155 140 160 0 210 Z" fill="url(#heroRed)"/>
      <path d="M0 210 C140 160 300 155 430 180 C520 200 600 215 717 205 V211 C600 222 520 207 430 187 C300 162 140 166 0 216 Z" fill="#e02a30"/>
    </svg>
    <h1 class="hero-title">Paint Protection<br>Options</h1>
    <svg class="hero-car" width="370" height="232" viewBox="0 0 370 232" role="img" aria-label="Photo of a glossy red hatchback car, front three-quarter view">
      <defs>
        <linearGradient id="carTone" x1="0" y1="0" x2="1" y2="1">
          <stop offset="0" stop-color="#e84a3a"/>
          <stop offset="0.5" stop-color="#c5211d"/>
          <stop offset="1" stop-color="#5e0a0a"/>
        </linearGradient>
      </defs>
      <path d="M10 160 C20 110 70 90 120 70 C160 30 210 10 280 12 C330 14 355 40 362 90 C368 140 350 200 300 222 C230 232 120 225 40 210 C15 200 5 180 10 160 Z" fill="url(#carTone)"/>
    </svg>
  </header>

  <h2 class="section-title ceramic-title"><span class="accent">Ceramic</span> Coatings</h2>
  <div class="section-text ceramic-text">
    <p>Ceramic coatings are liquid polymer coatings that bond to a vehicle’s painted surface. The coatings are formulated to retain the showroom finish by protecting against corrosion and contaminants like UV damage, oxidation, road salt and acid rain. Ceramic coatings give your car a deep, glossy finish that reflects light and makes your paint look more vibrant while greatly extending the paint's lifespan.</p>
    <p>The chemical bonding process improves color depth and leaves a smooth finish. The hydrophobic (water repellent) properties repel water and dirt as well as protect against damaging pollutants. This makes care and maintenance a breeze while retaining the show room finish. Never wax again!</p>
  </div>
  <svg class="photo-ring ceramic-photo" width="170" height="170" viewBox="0 0 170 170">
    <path d="M104 2 A83 83 0 1 0 104 168" fill="none" stroke="#000" stroke-width="2.5"/>
    <circle cx="90" cy="85" r="78" fill="#a3131a"/>
    <circle cx="90" cy="85" r="70" fill="#3b3f4a" role="img" aria-label="Photo of a technician polishing a red car with a machine polisher"/>
  </svg>

  <h2 class="section-title ppf-title"><span class="accent">Paint</span> Protection Film (PPF)</h2>
  <div class="section-text ppf-text">
    <p>Paint Protection Film (PPF) is a transparent, thermoplastic urethane film that is applied directly to the car’s painted surfaces. PPF excels at shielding your vehicle from rock chips, scratches, and other physical damage. It has self-healing properties that can repair minor scratches and swirl marks over time.</p>
    <p>Every piece of PPF is custom cut to fit each panel of your vehicle and provide maximum coverage. The film protects your vehicle from scratches, rock chips, staining, corrosion, fading, chemicals, insects, and road debris. It helps keep your paint looking new, saving you money and improving your resale value.</p>
  </div>
  <svg class="photo-ring ppf-photo" width="170" height="170" viewBox="0 0 170 170">
    <path d="M76 2 A83 83 0 1 1 76 168" fill="none" stroke="#000" stroke-width="2.5"/>
    <circle cx="90" cy="85" r="78" fill="#a3131a"/>
    <circle cx="90" cy="85" r="70" fill="#6b6e75" role="img" aria-label="Photo of hands applying clear protection film to a car hood with a spray bottle"/>
  </svg>

  <div class="compare">
    <div class="head">Feature</div>
    <div class="head flat">Car Wax</div>
    <div class="head">Ceramic Coating</div>
    <div class="head flat">Paint Protection Film</div>

    <div class="feature">Duration</div><div class="value">2 - 4 Weeks</div><div class="value">3 - 10 Years</div><div class="value">7 - 10 Years</div>
    <div class="feature">Thickness</div><div class="value">5 - 1.5 Microns</div><div class="value">7 - 10 Microns</div><div class="value">200 - 250 Microns</div>
    <div class="feature">Gloss Enhancement</div><div class="value">Full Circle - Green</div><div class="value">Full Circle - Green</div><div class="value">Full Circle - Green</div>
    <div class="feature">Acid Rain Damage</div><div class="value">1/2 Circle - Yellow</div><div class="value">Full Circle - Green</div><div class="value">Full Circle - Green</div>
    <div class="feature">Corrosion Prevention</div><div class="value">1/2 Circle - Yellow</div><div class="value">Full Circle - Green</div><div class="value">Full Circle - Green</div>
    <div class="feature">UV/Oxidation Protection</div><div class="value">1/2 Circle - Yellow</div><div class="value">Full Circle - Green</div><div class="value">Full Circle - Green</div>
    <div class="feature">Hard Water Damage</div><div class="value">1/4 Circle - Yellow</div><div class="value">3/4 Circle - Green</div><div class="value">Full Circle - Green</div>
    <div class="feature">Insect Splatter Damage</div><div class="value">1/4 Circle - Yellow</div><div class="value">3/4 Circle - Green</div><div class="value">Full Circle - Green</div>
    <div class="feature">Chip Protection</div><div class="value">Full Circle - Red</div><div class="value">1/4 Circle - Yellow</div><div class="value">Full Circle - Green</div>
    <div class="feature">Scratch Protection</div><div class="value">Full Circle - Red</div><div class="value">1/4 Circle - Yellow</div><div class="value">Full Circle - Green</div>
    <div class="feature">Swirl Protection</div><div class="value">Full Circle - Red</div><div class="value">Full Circle - Red</div><div class="value">Full Circle - Green</div>
    <div class="feature">Application Complexity</div><div class="value">Low</div><div class="value">Medium</div><div class="value">High</div>
  </div>
</main>
</body>
</html>
```